Car Wash - Total Redesign For New Owner - WIX or WordPress

Needs to be coded for WIX but will accept WordPress for outstanding designs.
This company has just been purchased and we now have a fresh logo to start off a totally new redesign of the web presence.
Sites I like:
https://www.vornatel.com.au/
https://www.qelro.com/au-en/
http://brindavex.com/#homepage1
https://www.plumtidecw.com.au/
What we sell can be found at the old website: www.glenshinewa.com.au
The package names have changed. Current package names uploaded "Price List.jpg"
I like the product descriptions at https://www.plumtidecw.com.au/
The new logo and prices have been uploaded. If it isn't on the price list, please don't carry it over from the old site.
The picture on the home page background should not be a car dashboard or an actual car wash. The image and the website will suggest luxury and having extra time to do things because you are not washing a car. Maybe you now have time to drive along a beautiful winding road by the sea? Or surprise me with an abstract background of colour or water droplets or something entirely different!
Please do something stunning that catches the eye. It must NOT look like I made it myself using a web building wizard.
Look at the websites I like - They will start you off.
Thanks and have fun!
Target Market(s)
We're selling a service that is geared for both male and females with higher incomes. They are 20-50 and usually have a car new car only a year or two old. They like nice ordered surroundings and a spotless car but don't have the time to clean it themselves.
Industry/Entity Type
Automotive
Requirements
Must have
- The theme is clean, easy to navigate but has a stunning visual impact.
- Online Bookings, Online Payment, Email Us
- Must look attractive and load quickly on mobile devices
- If you want a general idea of background image I think would be different for the home page, look at something similar to
- www.pixalund.com/pic-48210577/stock-photo-photo-of-water-splash-isolated-on-black.html?src=7kQwZrT2mLp9VxNcHsYbDa-1-64 would do it.
- I'm not saying you have to use this picture. Just be aware I want something different. I want to grab people's attention with something a bit different.
Nice to have
- Very clean on the home page. Possibly a background of moving water or water drops. Close-ups of: clean car interiors; polished and glossy external surfaces. The home page does not have to have a picture but can be an abstract design, close up of an object or material (water or soap). If there is a picture on the home page, the theme must be about relaxation, luxury, beauty.
Should not have
- No before/after pictures on the home page.
- On the home page, do not use a picture where the specific model of car is obvious. It makes the website look too much like a car dealership!

```html
<!DOCTYPE html>
<html lang="en">
<head>
<meta charset="utf-8">
<title>Glenshine WA – Automotive Detailing</title>
<link rel="stylesheet" href="https://fonts.googleapis.com/css2?family=Open+Sans:wght@400;600;700;800&family=Montserrat:wght@300;500&display=swap">
<style>
:root{
  --frame:#e6e6e6;
  --blue:#1a8fd0;
  --blue-dark:#0f5f94;
  --navy:#0d2f52;
  --ink:#3d3d3d;
  --rule:#cfd6dc;
  --dark:#1d1d1d;
  --dark-band:#252220;
  --grey-head:#9a9a9a;
  --white:#ffffff;
  --footer-text:#a9a9a9;
}
*{box-sizing:border-box;margin:0;padding:0}
html,body{width:1200px;height:2571px;overflow:hidden}
body{background:var(--frame);font-family:"Open Sans",sans-serif;color:var(--ink);position:relative}
.page{position:absolute;left:14px;top:14px;width:1172px;height:2543px;background:var(--white);overflow:hidden}

/* hero */
.hero{position:absolute;left:0;top:0;width:1172px;height:701px}
.hero-image{position:absolute;inset:0;background:
  radial-gradient(ellipse at 45% 30%,#cfe8f7 0%,rgba(150,205,240,.6) 22%,transparent 50%),
  radial-gradient(ellipse at 70% 85%,#0c5fa0 0%,transparent 55%),
  linear-gradient(180deg,#2f9ad9 0%,#5ab4e6 35%,#2c86c8 65%,#0b4f8e 100%)}
.brand{position:absolute;left:0;right:0;top:48px;display:flex;justify-content:center;align-items:center;gap:14px}
.brand-dot{width:22px;height:22px;border-radius:50%;background:var(--white)}
.brand-name{font-family:"Open Sans",sans-serif;font-weight:800;font-size:54px;color:var(--white);letter-spacing:1px;line-height:1}
.social-badge{position:absolute;right:16px;top:66px;width:118px;height:38px;border:2px solid var(--navy);background:rgba(255,255,255,.25);display:flex;align-items:center;gap:7px;padding-left:7px}
.social-badge span.box{width:20px;height:20px;background:var(--navy)}
.social-badge span.label{font-size:11px;font-weight:700;color:var(--navy);line-height:1.1}
.hero-title{position:absolute;left:0;right:0;top:440px;text-align:center;font-family:"Montserrat",sans-serif;font-weight:300;font-size:29px;letter-spacing:6px;color:var(--white)}
.hero-rule{position:absolute;left:366px;width:440px;top:490px;height:1px;background:rgba(255,255,255,.7)}
.main-nav{position:absolute;left:0;right:0;top:504px;display:flex;justify-content:center;gap:24px;font-family:"Montserrat",sans-serif;font-weight:500;font-size:15px;letter-spacing:.5px;color:var(--white)}
.main-nav a{color:inherit;text-decoration:none;padding-bottom:5px}
.main-nav a.current{border-bottom:2px solid var(--white)}

/* intro band */
.intro{position:absolute;left:0;top:701px;width:1172px;height:211px;background:linear-gradient(180deg,#2e2a27,#1b1918);display:flex;align-items:center}
.intro-heading{position:absolute;left:54px;top:56px;font-weight:700;font-size:29px;line-height:38px;text-transform:uppercase;color:var(--grey-head)}
.intro-heading strong{color:var(--white)}
.intro-heading em{font-style:normal;color:var(--blue)}
.intro-text{position:absolute;left:608px;top:72px;width:520px;font-size:15px;line-height:22px;font-weight:600;color:var(--white)}

/* section headings */
.section-title{position:absolute;left:0;right:0;text-align:center;font-size:28px;font-weight:600;color:#333;letter-spacing:.5px}
.section-title em{color:var(--blue);font-weight:700}
.divider{position:absolute;left:236px;width:700px;height:20px}
.divider::before{content:"";position:absolute;left:0;right:0;top:9px;height:1px;background:var(--rule)}
.divider::after{content:"";position:absolute;left:340px;top:0;width:20px;height:20px;border-radius:50%;background:var(--blue);box-shadow:0 0 0 6px var(--white)}

/* about */
.about-title{top:972px}
.about-divider{top:1019px}
.about-copy{position:absolute;left:112px;width:948px;top:1064px;text-align:center;font-size:14.6px;line-height:23px;color:#444}
.about-copy p+p{margin-top:23px}
.btn-book{position:absolute;left:440px;top:1302px;width:292px;height:40px;border-radius:4px;background:var(--blue);color:var(--white);font-weight:700;font-size:15px;display:flex;align-items:center;justify-content:center}

/* packages */
.packages-band{position:absolute;left:0;top:1472px;width:1172px;height:373px;background:linear-gradient(180deg,#2d94c9 0%,#4aa7d6 45%,#1f7fb8 100%)}
.package{position:absolute;top:1491px;width:252px;height:318px;border:2px solid rgba(255,255,255,.85);border-radius:8px;background:rgba(255,255,255,.22)}
.package-photo{position:absolute;top:-68px;left:50%;margin-left:-68px;width:136px;height:136px;border-radius:50%;border:6px solid var(--blue);box-shadow:0 0 0 3px var(--white)}
.package h3{position:absolute;top:80px;left:0;right:0;text-align:center;font-size:15px;font-weight:700;color:var(--navy)}
.package ul{position:absolute;top:102px;left:10px;right:10px;list-style:none;text-align:center;font-size:13px;line-height:20.5px;color:var(--white)}
.package .btn-more{position:absolute;left:56px;top:253px;width:140px;height:40px;border-radius:4px;background:var(--navy);color:var(--white);font-weight:700;font-size:15px;display:flex;align-items:center;justify-content:center}
.p1{left:56px}.p2{left:326px}.p3{left:596px}.p4{left:866px}
.p1 .package-photo{background:radial-gradient(circle at 55% 50%,#c9b64a,#2d4b66 70%)}
.p2 .package-photo{background:radial-gradient(circle at 50% 55%,#6d7f92,#1e2b3a 70%)}
.p3 .package-photo{background:radial-gradient(circle at 50% 50%,#a9d3ea,#3a6f9a 75%)}
.p4 .package-photo{background:radial-gradient(circle at 45% 55%,#f0e8e0,#c0302f 70%)}

/* clients */
.clients-title{top:1904px}
.clients-divider{top:1950px}
.client-row{position:absolute;left:130px;width:912px;top:2010px;height:100px;display:flex;justify-content:space-around;align-items:center}
.client{font-weight:800;font-size:30px;color:var(--navy)}
.client.alt{color:#111}
.client.green{color:#5a9a2e}
.carousel-arrow{position:absolute;top:2040px;width:24px;height:40px}
.arrow-prev{left:46px}.arrow-next{left:1102px}

/* footer */
.site-footer{position:absolute;left:0;top:2181px;width:1172px;height:325px;background:var(--dark);color:var(--footer-text)}
.footer-brand{position:absolute;left:42px;top:160px;display:flex;align-items:center;gap:10px}
.footer-brand .brand-dot{width:14px;height:14px;background:var(--blue)}
.footer-brand .brand-name{font-size:34px;color:var(--white)}
.footer-col h4{position:absolute;top:56px;font-size:16px;font-weight:700;color:var(--blue)}
.footer-col .col-rule{position:absolute;top:85px;height:1px;background:#3a3a3a}
.nav-col h4,.nav-col .col-rule{left:391px}.nav-col .col-rule{width:100px}
.contact-col h4,.contact-col .col-rule{left:571px}.contact-col .col-rule{width:220px}
.find-col h4,.find-col .col-rule{left:881px}.find-col .col-rule{width:250px}
.footer-links{position:absolute;left:391px;top:104px;list-style:none;font-size:13.5px;line-height:21px}
.contact-item{position:absolute;left:571px;display:flex;gap:12px;font-size:13.5px;line-height:19px}
.contact-item svg{flex:none;width:26px;height:26px}
.ci-1{top:102px}.ci-2{top:178px}.ci-3{top:216px}
.map{position:absolute;left:879px;top:100px;width:250px;height:180px;background:linear-gradient(135deg,#e9e6df,#d8d4ca)}
.copyright-bar{position:absolute;left:0;top:2506px;width:1172px;height:37px;background:var(--blue);color:var(--white)}
.copyright-bar p{position:absolute;left:34px;top:11px;font-size:11px;font-weight:700}
.social-dots{position:absolute;right:20px;top:9px;display:flex;gap:6px}
.social-dots span{width:19px;height:19px;border-radius:50%;background:var(--white)}
</style>
</head>
<body>
<div class="page">

  <header class="hero">
    <div class="hero-image" role="img" aria-label="Close-up of a blue water splash with droplets"></div>
    <div class="brand"><span class="brand-dot"></span><span class="brand-name">glenshine wa</span></div>
    <div class="social-badge"><span class="box"></span><span class="label">Find us on<br>Socials</span></div>
    <h1 class="hero-title">AUTOMOTIVE DETAILING</h1>
    <div class="hero-rule"></div>
    <nav class="main-nav">
      <a class="current">HOME</a><a>OUR PACKAGES</a><a>OUR CLIENTS</a><a>GALLERY</a><a>MAKE A BOOKING</a><a>FIND US</a>
    </nav>
  </header>

  <section class="intro">
    <h2 class="intro-heading">At <strong>Glenshine WA</strong>, there are<br>2 things we love the most;<br><em>cars and attention to detail.</em></h2>
    <p class="intro-text">That’s what makes us the preferred car washing and detailing specialist among WA’s leading car dealers and fleet companies, as well as the first choice among passionate motoring enthusiasts.</p>
  </section>

  <h2 class="section-title about-title">ABOUT <em>GLENSHINE WA</em></h2>
  <div class="divider about-divider"></div>
  <div class="about-copy">
    <p>We provide a range of service options to cater for the needs and budgets of our extensive and loyal customer base – from a simple wash through to a thorough detail, even scratch repairs. We even get the dirtiest 4WDs caked in red dust looking like new.</p>
    <p>With over 20 years experience, we adopt the very latest technologies, materials and techniques to help keep your much loved vehicle as shiny and new as the day you first met. As car enthusiasts, you’ll rest assured knowing that your pride and joy is taken care of, all the way, by our highly skilled technicians.</p>
    <p>And we’re conveniently located close to the Fernleigh Train Station on Kelvale Road in Ardenmoor. You can leave your vehicle in our capable hands, do your own thing and collect it from us when it’s ready. It’s that simple.</p>
  </div>
  <a class="btn-book">MAKE A BOOKING NOW!</a>

  <div class="packages-band" role="img" aria-label="Blurred photo of a clean car interior in blue tones"></div>
  <article class="package p1">
    <div class="package-photo" role="img" aria-label="Hand drying a car with a chamois"></div>
    <h3>Outside Wash Only</h3>
    <ul><li>• Full Service Hand Wash &amp;</li><li>Chamois Dry</li><li>• Chamois Dry</li><li>• Tyres Glossed</li></ul>
    <a class="btn-more">LEARN MORE</a>
  </article>
  <article class="package p2">
    <div class="package-photo" role="img" aria-label="Vacuuming a car seat"></div>
    <h3>The Mini Shine</h3>
    <ul><li>• Full Service Hand Wash &amp;</li><li>Chamois Dry</li><li>• Dust &amp; Condition All Vinyl &amp;</li><li>Leather Surfaces</li><li>• Through Vacuum</li></ul>
    <a class="btn-more">LEARN MORE</a>
  </article>
  <article class="package p3">
    <div class="package-photo" role="img" aria-label="Wiping a car dashboard with a cloth"></div>
    <h3>The Full Shine</h3>
    <ul><li>• Full Service Hand Wash &amp;</li><li>Chamois Dry</li><li>• Dust &amp; Condition All Vinyl &amp;</li><li>Leather Surfaces</li><li>• Special Vacuum for Sand &amp; Pet Hair</li><li>• Spot &amp; Stain Removal</li><li>• Wet &amp; Dry Foam Fabric Clean</li></ul>
    <a class="btn-more">LEARN MORE</a>
  </article>
  <article class="package p4">
    <div class="package-photo" role="img" aria-label="Gloved hand cleaning red leather"></div>
    <h3>Additional Services</h3>
    <ul><li>• Clay Bar Cleaning Treatment</li><li>• Fabric Seat Shampoo or Light</li><li>Stain Removal</li><li>• Leather Seat Clean &amp; Conditioning</li></ul>
    <a class="btn-more">LEARN MORE</a>
  </article>

  <h2 class="section-title clients-title">OUR <em>CLIENTS</em></h2>
  <div class="divider clients-divider"></div>
  <svg class="carousel-arrow arrow-prev" viewBox="0 0 24 40"><path d="M20 4 6 20l14 16" fill="none" stroke="#8a8a8a" stroke-width="4"/></svg>
  <div class="client-row">
    <span class="client">Halvord</span>
    <span class="client alt">Titan Motors</span>
    <span class="client">Northgate Autos</span>
    <span class="client green">Corvane</span>
  </div>
  <svg class="carousel-arrow arrow-next" viewBox="0 0 24 40"><path d="M4 4l14 16L4 36" fill="none" stroke="#8a8a8a" stroke-width="4"/></svg>

  <footer class="site-footer">
    <div class="footer-brand"><span class="brand-dot"></span><span class="brand-name">glenshine wa</span></div>
    <div class="footer-col nav-col"><h4>Navigation</h4><div class="col-rule"></div></div>
    <ul class="footer-links"><li>Home</li><li>Packages</li><li>Our Clients</li><li>Gallery</li><li>Make a Booking</li><li>Contact Us</li></ul>
    <div class="footer-col contact-col"><h4>Contact Us</h4><div class="col-rule"></div></div>
    <div class="contact-item ci-1">
      <svg viewBox="0 0 26 26"><circle cx="13" cy="13" r="12" fill="none" stroke="#1a8fd0" stroke-width="1.6"/><path d="M13 6a4.5 4.5 0 0 0-4.5 4.5C8.5 14 13 20 13 20s4.5-6 4.5-9.5A4.5 4.5 0 0 0 13 6z" fill="#1a8fd0"/><circle cx="13" cy="10.5" r="1.6" fill="#1d1d1d"/></svg>
      <span>GLENSHINE WA<br>412 Kelvale Road<br>Ardenmoor WA 6018</span>
    </div>
    <div class="contact-item ci-2">
      <svg viewBox="0 0 26 26"><circle cx="13" cy="13" r="12" fill="none" stroke="#1a8fd0" stroke-width="1.6"/><path d="M9 7l2.5 0 1 3-1.5 1.2a7 7 0 0 0 3.8 3.8L16 13.5l3 1v2.5c-6 .5-10.5-4-10-10z" fill="#1a8fd0"/></svg>
      <span style="padding-top:4px">Sam: 0400 555 019</span>
    </div>
    <div class="contact-item ci-3">
      <svg viewBox="0 0 26 26"><circle cx="13" cy="13" r="12" fill="none" stroke="#1a8fd0" stroke-width="1.6"/><circle cx="13" cy="13" r="7" fill="none" stroke="#1a8fd0" stroke-width="1.6"/><path d="M13 9v4.5l3 1.5" fill="none" stroke="#1a8fd0" stroke-width="1.6"/></svg>
      <span>Opening Hours:<br>Mondays – Fridays: 8am – 5pm<br>Saturdays: 8am – 1pm</span>
    </div>
    <div class="footer-col find-col"><h4>Find Us</h4><div class="col-rule"></div></div>
    <div class="map" role="img" aria-label="Street map showing the workshop location"></div>
  </footer>
  <div class="copyright-bar">
    <p>COPYRIGHT © 2016 GLENSHINE WA. ALL RIGHTS RESERVED.</p>
    <div class="social-dots"><span></span><span></span><span></span></div>
  </div>

</div>
</body>
</html>
```